Business Card Design

Business Card for professional consulting firm working with large financial institutions.

Target Market(s)

Executive buyers

Industry/Entity Type

Banking

Contact Information for Business Card

Mild creativity wanted. Not boring, but do elaborate artwork.

Font styles to use
Serif
Sans Serif

Colors

Designer to choose colors to be used in the design.

Requirements
Must have
• Standard business card features - company name, individual name, telephone, website, email, locations.
Nice to have
• Two colors
Should not have
• too many colors, fancy printing, cartoons.

```html
<!DOCTYPE html>
<html lang="en">
<head>
<meta charset="UTF-8">
<title>Northvale Advisory — Business Card</title>
<link href="https://fonts.googleapis.com/css2?family=Open+Sans:wght@400;600;700&display=swap" rel="stylesheet">
<style>
  :root {
    --backdrop: #2b2d31;
    --card: #050505;
    --accent-red: #ee1c25;
    --text-white: #ffffff;
    --text-light: #d9d9d9;
    --text-muted: #8a8a8a;
    --mark-grey: #7d8083;
  }
  * { margin: 0; padding: 0; box-sizing: border-box; }
  html, body {
    width: 1200px;
    height: 900px;
    overflow: hidden;
    background: var(--backdrop);
    font-family: "Open Sans", Arial, sans-serif;
  }
  .stage {
    position: relative;
    width: 1200px;
    height: 900px;
  }
  .card {
    position: absolute;
    width: 600px;
    height: 343px;
    background: var(--card);
    border-radius: 4px;
    overflow: hidden;
    box-shadow: 0 18px 40px rgba(0,0,0,0.45);
  }

  /* Front side */
  .card--front { left: 300px; top: 70px; }
  .card--front .brand {
    position: absolute;
    left: 0; right: 0;
    top: 120px;
    display: flex;
    align-items: center;
    justify-content: center;
    gap: 14px;
  }
  .brand-dot {
    width: 14px; height: 14px;
    border-radius: 50%;
    background: var(--mark-grey);
  }
  .brand-name {
    font-weight: 600;
    color: var(--text-white);
    letter-spacing: 0.5px;
  }
  .card--front .brand-name { font-size: 34px; }
  .card--front .website {
    position: absolute;
    left: 0; right: 0;
    top: 215px;
    text-align: center;
    font-size: 20px;
    color: var(--text-light);
    letter-spacing: 0.5px;
  }
  .card--front .edge-band {
    position: absolute;
    left: 0; right: 0;
    bottom: 0;
    height: 36px;
    background: var(--accent-red);
  }

  /* Back side */
  .card--back { left: 300px; top: 487px; }
  .card--back .band {
    position: absolute;
    left: 0;
    top: 150px;
    width: 330px;
    height: 36px;
    background: var(--accent-red);
  }
  .card--back .brand {
    position: absolute;
    left: 344px;
    top: 150px;
    height: 36px;
    display: flex;
    align-items: center;
    gap: 8px;
  }
  .card--back .brand-dot { width: 10px; height: 10px; }
  .card--back .brand-name { font-size: 18px; }
  .holder {
    position: absolute;
    right: 40px;
    top: 56px;
    text-align: left;
    color: var(--text-white);
  }
  .holder-name { font-size: 22px; font-weight: 700; line-height: 1.2; }
  .holder-position { font-size: 20px; font-weight: 400; line-height: 1.2; }
  .contact {
    position: absolute;
    left: 36px;
    top: 212px;
    font-size: 13px;
    line-height: 20px;
    color: var(--text-muted);
  }
  .contact-row { display: flex; }
  .contact-label { width: 62px; }
</style>
</head>
<body>
  <main class="stage">
    <section class="card card--front" aria-label="Card front">
      <div class="brand">
        <span class="brand-dot"></span>
        <span class="brand-name">Northvale Advisory</span>
      </div>
      <p class="website">www.website.com</p>
      <div class="edge-band"></div>
    </section>

    <section class="card card--back" aria-label="Card back">
      <div class="holder">
        <p class="holder-name">Name</p>
        <p class="holder-position">position</p>
      </div>
      <div class="band"></div>
      <div class="brand">
        <span class="brand-dot"></span>
        <span class="brand-name">Northvale Advisory</span>
      </div>
      <div class="contact">
        <div class="contact-row"><span class="contact-label">Addess</span></div>
        <div class="contact-row"><span class="contact-label">Tel</span><span>: 00 000 000</span></div>
        <div class="contact-row"><span class="contact-label">Mob</span><span>: 00 000 000</span></div>
        <div class="contact-row"><span class="contact-label">E-mail</span><span>: youremail@address</span></div>
        <div class="contact-row"><span class="contact-label">Web</span><span>: www.yourwebaddress</span></div>
      </div>
    </section>
  </main>
</body>
</html>
```